Psychology Practice in Sydney Website Redesign

Corlew Psychology is a Psychology Practice with locations in Westmead, Chatswood and the CBD. They have specialties in treating children, and in treating eating disorders. They also treat anxiety and depression. They have ~10-20 clinical psychologists working for them.

The client wants the site to be modern and professional, he said:
”Mainly gonna be the credibility, people already know of us, but some could find us on google search, site needs to be a bit sexy.”

The client prefers websites with a heavy use of negative space and a largely minimal, modern design. (e.g. https://harbourlanemind-example.com.au/, https://www.fenmora-example.net.au/, https://tovalin-example.com.au/). He wants the site to be approachable without being unprofessional, and to be modern without being clinical. This is their current site: https://www.corlewpsychology-example.com.au/

The client wants the site to be a one pager design (like the sites given above). Please include a section named “Our Specialisations”, and the next titled “What we treat”, then one titled “Our Team” Feel free to take inspiration from the included links for the layout of these parts of the site.

Please mock up a booking panel similar to the that appears when you click "book now" on https://www.quillbrookcare-example.com.au/# .

The client would prefer you use the current logo and colour green (in logo) for theming.

Current site: https://www.corlewpsychology-example.com.au/

The winning designers will be required to:
- Provide a secondary standard page template
- Provide a design for a flyout enquiry/booking form
- Supply all images used in the designs free of charge

```html
<!DOCTYPE html>
<html lang="en">
<head>
<meta charset="utf-8">
<title>Corlew &amp; Associates — Contact</title>
<link href="https://fonts.googleapis.com/css2?family=Open+Sans:wght@400;600;700&display=swap" rel="stylesheet">
<style>
  :root {
    --page-dim: #ababab;
    --ink: #1f1f1f;
    --panel: #f3f3f3;
    --green: #6cc08a;
    --green-btn: #7cc594;
    --field-border: #7fca98;
    --muted: #7a7a7a;
    --brand: #4f8a63;
  }
  * { box-sizing: border-box; margin: 0; padding: 0; }
  html, body { width: 1200px; height: 1045px; overflow: hidden; }
  body {
    position: relative;
    background: var(--page-dim);
    font-family: "Open Sans", sans-serif;
    color: var(--ink);
  }
  .brand {
    position: absolute; left: 42px; top: 22px;
    font-size: 17px; font-weight: 700; color: var(--brand);
    display: flex; align-items: center; gap: 7px;
  }
  .brand-mark { width: 12px; height: 12px; background: var(--brand); }
  .main-nav {
    position: absolute; top: 31px; left: 463px;
    display: flex; gap: 20px; font-size: 12px; font-weight: 600;
  }
  .hero-title {
    position: absolute; left: 42px; top: 150px;
    font-size: 92px; font-weight: 600; line-height: 84px; letter-spacing: -1px;
  }
  .hero-photo {
    position: absolute; left: 42px; top: 379px; width: 1120px; height: 664px;
    border-radius: 10px;
    background: linear-gradient(160deg, #8d8f8f 0%, #9a9a96 40%, #6f665b 75%, #4c3a2b 100%);
  }
  .contact-panel {
    position: absolute; left: 669px; top: 21px; width: 545px; height: 1002px;
    background: var(--panel); border-radius: 13px;
  }
  .contact-panel > * { position: absolute; line-height: 1; }
  .close-btn { left: 500px; top: 20px; width: 14px; height: 14px; }
  .panel-title {
    left: 0; width: 531px; top: 68px; text-align: center;
    font-size: 42px; font-weight: 700;
  }
  .panel-sub {
    left: 0; width: 531px; top: 131px; text-align: center;
    font-size: 15.5px; font-weight: 400;
  }
  .field-label { font-size: 13.5px; font-weight: 400; }
  .field {
    height: 42px; width: 205px;
    border: 1px solid var(--field-border); border-radius: 3px; background: var(--panel);
  }
  .field-wide { width: 428px; }
  .select-text { position: absolute; left: 12px; top: 13px; font-size: 13.5px; line-height: 1; }
  .select-chev { position: absolute; right: 14px; top: 17px; }
  .message { height: 152px; }
  .placeholder { position: absolute; left: 12px; top: 13px; font-size: 13.5px; line-height: 1; color: var(--muted); }
  .option { display: flex; align-items: center; gap: 9px; font-size: 14px; height: 17px; }
  .radio { width: 17px; height: 17px; border: 1.5px solid #222; border-radius: 50%; flex: none; }
  .terms { left: 53px; top: 874px; display: flex; align-items: center; gap: 7px; font-size: 12px; }
  .terms u { text-underline-offset: 2px; }
  .submit {
    left: 222px; top: 924px; width: 90px; height: 42px;
    border-radius: 21px; background: var(--green-btn); color: #fff;
    font-size: 14px; font-weight: 700; display: flex; align-items: center; justify-content: center;
  }
</style>
</head>
<body>
  <div class="brand"><span class="brand-mark"></span>Corlew &amp; Associates</div>
  <nav class="main-nav"><span>About</span><span>Services</span><span>What We Treat</span></nav>
  <h1 class="hero-title">Care that<br>transforms</h1>
  <div class="hero-photo" role="img" aria-label="Psychologist seated in a wooden armchair taking notes beside a bright window"></div>

  <aside class="contact-panel">
    <svg class="close-btn" viewBox="0 0 14 14"><path d="M1 1L13 13M13 1L1 13" stroke="#6cc08a" stroke-width="1.8"/></svg>
    <h2 class="panel-title">Contact us</h2>
    <p class="panel-sub">You are not alone</p>

    <label class="field-label" style="left:53px;top:194px">First name</label>
    <div class="field" style="left:53px;top:216px"></div>
    <label class="field-label" style="left:276px;top:194px">Last name</label>
    <div class="field" style="left:276px;top:216px"></div>

    <label class="field-label" style="left:53px;top:280px">Email</label>
    <div class="field" style="left:53px;top:303px"></div>
    <label class="field-label" style="left:276px;top:280px">Phone number</label>
    <div class="field" style="left:276px;top:303px"></div>

    <label class="field-label" style="left:53px;top:367px">Choose a topic</label>
    <div class="field field-wide" style="left:53px;top:390px">
      <span class="select-text">Select one...</span>
      <svg class="select-chev" width="10" height="7" viewBox="0 0 10 7"><path d="M1 1L5 5L9 1" stroke="#6cc08a" stroke-width="1.5" fill="none"/></svg>
    </div>

    <p class="field-label" style="left:53px;top:467px">Which best describes you?</p>
    <div class="option" style="left:53px;top:499px"><span class="radio"></span>Mood</div>
    <div class="option" style="left:53px;top:531px"><span class="radio"></span>Anxiety</div>
    <div class="option" style="left:53px;top:563px"><span class="radio"></span>Eating Disorders</div>
    <div class="option" style="left:53px;top:594px"><span class="radio"></span>Trauma</div>
    <div class="option" style="left:53px;top:626px"><span class="radio"></span>Physical Health</div>
    <div class="option" style="left:276px;top:499px"><span class="radio"></span>Trauma</div>
    <div class="option" style="left:276px;top:531px"><span class="radio"></span>Physical Health</div>
    <div class="option" style="left:276px;top:563px"><span class="radio"></span>Self-esteem</div>
    <div class="option" style="left:276px;top:592px"><span class="radio"></span>Child and Family Services</div>
    <div class="option" style="left:276px;top:626px"><span class="radio"></span>Other</div>

    <label class="field-label" style="left:53px;top:680px">Message</label>
    <div class="field field-wide message" style="left:53px;top:703px"><span class="placeholder">Type your message...</span></div>

    <div class="terms"><span class="radio"></span><span>I accept the <u>Terms</u></span></div>
    <div class="submit">Submit</div>
  </aside>
</body>
</html>
```